Criação de Cartao de Visita para Vigor & Equilíbrio
" Venda de Suplementos Alimentares/Nutricionais, principalmente via whatsapp e facebook, fazemos entregas e aceitamos cartões. Ainda não possuimos loja física. Cobrimos qualquer oferta de site ou loja nacional. "

```html
<!DOCTYPE html>
<html lang="pt-BR">
<head>
<meta charset="UTF-8">
<title>Vigor &amp; Equilíbrio — Cartão de Visita</title>
<link href="https://fonts.googleapis.com/css2?family=Montserrat:wght@800&family=Roboto:wght@400;700&display=swap" rel="stylesheet">
<style>
  :root {
    --stage: #e9e7e4;
    --paper: #ffffff;
    --ink: #1a1a1a;
    --gold: #e0a21b;
    --gold-light: #f6c544;
    --night: #141414;
    --night-mid: #2a2a2a;
  }
  * { margin: 0; padding: 0; box-sizing: border-box; }
  html, body { width: 1200px; height: 1200px; overflow: hidden; }
  body {
    background: var(--stage);
    font-family: "Roboto", Arial, sans-serif;
    color: var(--ink);
    position: relative;
  }
  .card {
    position: absolute;
    left: 150px;
    width: 900px;
    height: 500px;
    overflow: hidden;
    box-shadow: 0 10px 30px rgba(0,0,0,.18);
  }
  /* Verso: contatos */
  .card--contact { top: 70px; background: var(--paper); }
  .card--contact .edge-band {
    position: absolute; left: 0; bottom: 0; width: 100%; height: 14px;
    background: var(--gold);
  }
  .brand {
    display: flex; align-items: center; gap: 16px;
    font-family: "Montserrat", sans-serif; font-weight: 800;
    color: var(--gold); text-transform: uppercase; letter-spacing: 1px;
  }
  .brand__dot { border-radius: 50%; background: var(--gold); flex: none; }
  .card--contact .brand {
    position: absolute; left: 60px; top: 200px; font-size: 34px;
  }
  .card--contact .brand__dot { width: 64px; height: 64px; }
  .holder {
    position: absolute; right: 60px; top: 150px; text-align: right;
  }
  .holder__name { font-weight: 700; font-size: 20px; letter-spacing: 1px; }
  .holder__role { font-size: 14px; letter-spacing: 1px; margin-top: 2px; }
  .contact-list {
    position: absolute; right: 60px; top: 225px; list-style: none;
  }
  .contact-list li {
    display: flex; justify-content: flex-end; align-items: center; gap: 12px;
    font-size: 17px; font-weight: 700; line-height: 1.15; margin-bottom: 8px;
    text-align: right;
  }
  .contact-icon {
    width: 22px; height: 22px; background: var(--gold); border-radius: 3px;
    flex: none; display: flex; align-items: center; justify-content: center;
  }
  /* Frente: marca */
  .card--brand { top: 630px; background: var(--night); }
  .texture {
    position: absolute; inset: 0;
    background: radial-gradient(ellipse at 50% 45%, var(--night-mid) 0%, var(--night) 70%);
  }
  .card--brand .brand {
    position: absolute; left: 0; right: 0; top: 200px; justify-content: center;
    font-size: 52px;
  }
  .card--brand .brand__dot { width: 90px; height: 90px; background: var(--gold-light); }
</style>
</head>
<body>
  <section class="card card--contact">
    <div class="brand"><span class="brand__dot"></span>Vigor &amp; Equilíbrio</div>
    <div class="holder">
      <p class="holder__name">NOME SOBRENOME</p>
      <p class="holder__role">FUNÇÃO</p>
    </div>
    <ul class="contact-list">
      <li>contato@vigorequilibrio.com.br
        <span class="contact-icon"><svg width="14" height="10" viewBox="0 0 14 10"><rect x="0.5" y="0.5" width="13" height="9" fill="none" stroke="#fff"/><path d="M0.5 0.5 7 6 13.5 0.5" fill="none" stroke="#fff"/></svg></span></li>
      <li>www.vigorequilibrio.com.br
        <span class="contact-icon"><svg width="14" height="14" viewBox="0 0 14 14"><circle cx="7" cy="7" r="6" fill="none" stroke="#fff"/><ellipse cx="7" cy="7" rx="2.5" ry="6" fill="none" stroke="#fff"/><path d="M1 7h12" stroke="#fff"/></svg></span></li>
      <li>(11) 98765-4321
        <span class="contact-icon"><svg width="12" height="14" viewBox="0 0 12 14"><path d="M2 1h3l1 3-2 1.5c.8 1.8 1.8 2.8 3.5 3.5L9 7l3 1v3c0 1-1 2-2 2C5 13 0 8 0 3c0-1 1-2 2-2z" fill="#fff"/></svg></span></li>
      <li>(11) 91234-5678
        <span class="contact-icon"><svg width="10" height="14" viewBox="0 0 10 14"><rect x="0.5" y="0.5" width="9" height="13" rx="1.5" fill="none" stroke="#fff"/><circle cx="5" cy="11" r="1" fill="#fff"/></svg></span></li>
      <li>Endereço Completo, 000 Bairro<br>Cidade/Estado
        <span class="contact-icon"><svg width="10" height="14" viewBox="0 0 10 14"><path d="M5 14S0 8 0 5a5 5 0 0 1 10 0c0 3-5 9-5 9z" fill="#fff"/><circle cx="5" cy="5" r="1.8" fill="var(--gold)"/></svg></span></li>
    </ul>
    <div class="edge-band"></div>
  </section>

  <section class="card card--brand">
    <div class="texture" role="img" aria-label="Textura metálica escura em padrão de colmeia"></div>
    <div class="brand"><span class="brand__dot"></span>Vigor &amp; Equilíbrio</div>
  </section>
</body>
</html>
```